Re-Design my old Business Card

We need a new business card design. The current layout is lacking good design.
We manufacture building products and also offers services (www.tormavestructures.com.au)
I've attached the old business card to show you what we don't want.
I've also attached the new logo in two styles for you to chose from.
The final design should communicate smarter building design and lifestyle, with a clean and crisp designed card.

Target Market(s)

Architects, building companies

Industry/Entity Type

Business

Contact Information for Business Card

See attached old business cards for all details to include

Font styles to use
Sans Serif

Colors
9bcb3b

Requirements
Must have
• Clean crisp look
Nice to have
• Totally up to you

```html
<!DOCTYPE html>
<html lang="en">
<head>
<meta charset="utf-8">
<title>Dale Ostrander — Business Card</title>
<link rel="stylesheet" href="https://fonts.googleapis.com/css2?family=Questrial&family=Montserrat:wght@700&display=swap">
<style>
  :root {
    --brand-green: #9ecb3d;
    --card-text: #ffffff;
    --page-bg: #ffffff;
  }
  html, body {
    margin: 0;
    padding: 0;
    width: 1200px;
    height: 1000px;
    overflow: hidden;
    background: var(--page-bg);
  }
  .business-card {
    position: absolute;
    left: 94px;
    top: 176px;
    width: 1004px;
    height: 649px;
    background: var(--brand-green);
    color: var(--card-text);
    font-family: "Questrial", "Century Gothic", sans-serif;
  }
  .holder-name {
    position: absolute;
    left: 59px;
    top: 56px;
    margin: 0;
    font-family: "Montserrat", "Century Gothic", sans-serif;
    font-weight: 700;
    font-size: 31px;
    letter-spacing: 1.5px;
    line-height: 40px;
  }
  .holder-role {
    position: absolute;
    left: 59px;
    top: 104px;
    margin: 0;
    font-size: 27px;
    line-height: 36px;
  }
  .contact-list {
    position: absolute;
    left: 59px;
    top: 186px;
    margin: 0;
    display: grid;
    grid-template-columns: 128px auto;
    font-size: 25px;
    line-height: 37.5px;
  }
  .contact-list dt,
  .contact-list dd {
    margin: 0;
  }
  .office-address {
    position: absolute;
    left: 59px;
    top: 494px;
    margin: 0;
    font-style: normal;
    font-size: 24px;
    line-height: 33px;
  }
</style>
</head>
<body>
  <section class="business-card">
    <h1 class="holder-name">DALE OSTRANDER</h1>
    <p class="holder-role">Account Manager Qld / Northern NSW</p>

    <dl class="contact-list">
      <dt>Mobile</dt><dd>0491 627 384</dd>
      <dt>Phone</dt><dd>1300 472 905</dd>
      <dt>Fax</dt><dd>1300 472 905</dd>
      <dt>Email</dt><dd>dale@tormavestructures.com.au</dd>
    </dl>

    <address class="office-address">
      Unit 2/18 Carrow Street<br>
      Head Office<br>
      Kingsbrook, QLD 4132
    </address>
  </section>
</body>
</html>
```